Flyer

I am a qualified accountant and I need a flyer to promote my business when networking

My services include
Management Accounts, Financial Accounts, Day to Day Bookkeeping services, business start up assistance
I will produce and submit Self Assessment Tax Returns, Annual Accounts, VAT tax returns, Payroll and PAYE

I attach my business card design so that there is some continuity if you think it appropiate.

Size A3 is preferred, please.

Sorry, I mean't Size A5 is preferred.

A5 please

Free initial consultations and advice.

```html
<!DOCTYPE html>
<html lang="en">
<head>
<meta charset="utf-8">
<title>Clare Whitfield Accounting – Flyer</title>
<link rel="stylesheet" href="https://fonts.googleapis.com/css2?family=Cinzel:wght@400;500&family=Roboto:wght@400;500&family=Exo+2:ital,wght@1,400&display=swap">
<style>
  :root {
    --lime: #c3d935;
    --leaf: #8dc63f;
    --navy: #1f3a8c;
    --ink: #2b2b2b;
    --paper: #ffffff;
    --mist: #eeeff1;
    --white: #ffffff;
  }
  * { margin: 0; padding: 0; box-sizing: border-box; }
  html, body { width: 893px; height: 1200px; overflow: hidden; background: var(--paper); }
  .flyer { position: relative; width: 893px; height: 1200px; overflow: hidden; background: var(--paper); font-family: "Roboto", sans-serif; }

  .hero-photo { position: absolute; left: 0; top: 0; width: 893px; height: 540px; }

  .brand { position: absolute; left: 0; top: 600px; width: 893px; text-align: center; }
  .brand-name { font-family: "Cinzel", serif; font-weight: 400; font-size: 24px; letter-spacing: 0.5px; color: var(--ink); }
  .brand-tagline { font-family: "Roboto", sans-serif; font-size: 13px; color: var(--ink); margin-top: 2px; }
  .brand-dot { display: block; width: 44px; height: 44px; border-radius: 50%; background: var(--leaf); margin: 0 auto 10px; }

  .services-band { position: absolute; left: 0; top: 720px; width: 893px; height: 405px; }

  .services { position: absolute; left: 40px; top: 784px; list-style: none; }
  .services li { position: relative; padding-left: 24px; font-size: 19.5px; line-height: 24px; color: var(--navy); margin-bottom: 10px; }
  .services li svg { position: absolute; left: 0; top: 5px; }

  .handshake-photo { position: absolute; left: 426px; top: 793px; width: 426px; height: 268px; }

  .band-tagline { position: absolute; left: 431px; top: 1074px; width: 420px; text-align: center; font-family: "Exo 2", sans-serif; font-style: italic; font-size: 30px; color: var(--white); }

  .contact-bar { position: absolute; left: 0; top: 1125px; width: 893px; height: 62px; background: var(--mist); display: flex; align-items: center; padding-left: 42px; }
  .contact-name { font-family: "Cinzel", serif; font-size: 24px; color: var(--ink); width: 345px; white-space: nowrap; }
  .contact-name small { font-size: 16px; }
  .contact-item { display: flex; align-items: center; gap: 6px; font-weight: 500; color: var(--ink); }
  .contact-phone { font-size: 18px; width: 175px; }
  .contact-email { font-size: 14.5px; }
  .footer-strip { position: absolute; left: 0; top: 1187px; width: 893px; height: 13px; background: var(--leaf); }
</style>
</head>
<body>
<main class="flyer">
  <svg class="hero-photo" viewBox="0 0 893 540" role="img" aria-label="Photo of hands using a calculator over financial paperwork">
    <defs>
      <linearGradient id="heroTone" x1="0" y1="0" x2="1" y2="1">
        <stop offset="0" stop-color="#e9ecef"/>
        <stop offset="0.45" stop-color="#c9ccd0"/>
        <stop offset="0.7" stop-color="#5b5e63"/>
        <stop offset="1" stop-color="#dfe2e6"/>
      </linearGradient>
    </defs>
    <path d="M0 0H893V489H683L656 540H250L204 489H0Z" fill="url(#heroTone)"/>
  </svg>

  <svg class="services-band" viewBox="0 0 893 405" aria-hidden="true">
    <rect x="0" y="45" width="893" height="360" fill="var(--lime)"/>
    <path d="M0 0H204L245 45H652L692 0H893V45H0Z" fill="var(--leaf)"/>
  </svg>

  <div class="brand">
    <span class="brand-dot"></span>
    <div class="brand-name">Clare Whitfield Accounting</div>
    <div class="brand-tagline">Making Accounts look easy</div>
  </div>

  <ul class="services">
    <li><svg width="20" height="16" viewBox="0 0 20 16"><path d="M1 8l6 6L19 1" fill="none" stroke="var(--navy)" stroke-width="3"/></svg>Management Accounting</li>
    <li><svg width="20" height="16" viewBox="0 0 20 16"><path d="M1 8l6 6L19 1" fill="none" stroke="var(--navy)" stroke-width="3"/></svg>Financial Accounting</li>
    <li><svg width="20" height="16" viewBox="0 0 20 16"><path d="M1 8l6 6L19 1" fill="none" stroke="var(--navy)" stroke-width="3"/></svg>Budgeting</li>
    <li><svg width="20" height="16" viewBox="0 0 20 16"><path d="M1 8l6 6L19 1" fill="none" stroke="var(--navy)" stroke-width="3"/></svg>Day to Day Bookkeeping Services</li>
    <li><svg width="20" height="16" viewBox="0 0 20 16"><path d="M1 8l6 6L19 1" fill="none" stroke="var(--navy)" stroke-width="3"/></svg>Business start up assitance</li>
    <li><svg width="20" height="16" viewBox="0 0 20 16"><path d="M1 8l6 6L19 1" fill="none" stroke="var(--navy)" stroke-width="3"/></svg>Production and submission of<br>Self Assessment Tax Returns</li>
    <li><svg width="20" height="16" viewBox="0 0 20 16"><path d="M1 8l6 6L19 1" fill="none" stroke="var(--navy)" stroke-width="3"/></svg>VAT returns</li>
    <li><svg width="20" height="16" viewBox="0 0 20 16"><path d="M1 8l6 6L19 1" fill="none" stroke="var(--navy)" stroke-width="3"/></svg>Annual Accounts</li>
    <li><svg width="20" height="16" viewBox="0 0 20 16"><path d="M1 8l6 6L19 1" fill="none" stroke="var(--navy)" stroke-width="3"/></svg>Payroll &amp; PAYE</li>
  </ul>

  <svg class="handshake-photo" viewBox="0 0 426 268" role="img" aria-label="Photo of a business handshake between office towers against the sky">
    <defs>
      <linearGradient id="skyTone" x1="0" y1="0" x2="1" y2="1">
        <stop offset="0" stop-color="#4d5d6e"/>
        <stop offset="0.45" stop-color="#d7e0ea"/>
        <stop offset="0.75" stop-color="#b86a4f"/>
        <stop offset="1" stop-color="#3b3d42"/>
      </linearGradient>
    </defs>
    <rect width="426" height="268" fill="url(#skyTone)"/>
  </svg>

  <div class="band-tagline">Making Accounts look easy</div>

  <footer class="contact-bar">
    <div class="contact-name">Clare Whitfield <small>ACMA, CGMA</small></div>
    <div class="contact-item contact-phone">
      <svg width="16" height="16" viewBox="0 0 16 16"><circle cx="8" cy="8" r="7" fill="none" stroke="var(--ink)" stroke-width="1.2"/><path d="M5.5 4.5l1.5 0.5-0.5 2 1.8 2 2-0.5 0.5 1.5-1.5 1c-3 0-5-3-5-5z" fill="var(--ink)"/></svg>
      07700 900123
    </div>
    <div class="contact-item contact-email">
      <svg width="20" height="14" viewBox="0 0 20 14"><rect x="1" y="1" width="18" height="12" fill="none" stroke="var(--ink)" stroke-width="1.6"/><path d="M1 1l9 7 9-7" fill="none" stroke="var(--ink)" stroke-width="1.6"/></svg>
      clare@whitfieldaccounts.co.uk
    </div>
  </footer>
  <div class="footer-strip"></div>
</main>
</body>
</html>
```